Specialised Shopfitting Hardware Wholesaler Needs Business Card Design

We need a business card design for our dual businesses.

One side is Corvane Doors also called 'CD' mostly known in the industry as 'Corvane'. One of only a few companies in the state the produce custom doors, we have been in business for 15 years.
We manufacture commercial fridge doors for custom made fridges.
Door types are: Insert doors, swing doors, sliding doors.
Our advertising is word of mouth only as we know almost all the shopfitters in the state, and they are mostly aware of our products.

We are building a website to make it easier for our customers to show their customers our range of products and applications.

I know it's sounds weird to have all of that on a card, but i'd rather be over descriptive than under.

UPDATE: I have decided to just go with the one business for now.
I uploaded the current card design. I would like it with the same layout, info on the front and description of our products on the back.

Industry/Entity Type

Business

Contact Information for Business Card

For Corvane Doors:
Name: Brent Oakley
Address: 417 Harwick Vale Rd, Tamsley, NSW 2874
Phone: (02) 4893 5100
Fax: (02) 4893 5177
Mobile: 0400 58 3232

Requirements
Must have
• FRONT: Name, email, phone, fax and mobile number.
• Company url : www.corvanedoors-example.com.au
• BACK:
• Stainless Steel Refrigeration Doors
• Double & Triple Glazed Refrigeration Doors
• Heated Glass Refrigeration Doors
• Inserts for both Under-bar and Coolroom
• Single & Double Glazed Sliding Doors
• Super View Panels
• Hood Light Covers
• LED and Fluro Lights for Cold Food & Cake Display
• Heat Lamps for Bain-marie and Pies

```html
<!DOCTYPE html>
<html lang="en">
<head>
<meta charset="utf-8">
<title>Corvane Doors – Business Card</title>
<link rel="stylesheet" href="https://fonts.googleapis.com/css2?family=Questrial&family=Tinos&display=swap">
<style>
  :root {
    --stage: #2e2e30;
    --navy: #1d3f7e;
    --blue: #2f5da8;
    --ink: #1f3566;
    --sage: #c7d2c6;
    --sage-soft: #dbe3da;
    --band-grey: #9c9c9c;
    --card-white: #ffffff;
  }
  * { box-sizing: border-box; margin: 0; padding: 0; }
  html, body {
    width: 1200px; height: 1000px; overflow: hidden;
    background: var(--stage);
  }
  .stage { position: relative; width: 1200px; height: 1000px; }
  .card {
    position: absolute; left: 195px; width: 810px; height: 450px;
    overflow: hidden;
  }

  /* Back: product list */
  .card-back { top: 30px; background: var(--sage); }
  .product-list {
    list-style: none; text-align: center;
    font-family: "Tinos", "Times New Roman", serif;
    font-size: 24px; line-height: 44px; color: var(--ink);
    padding-top: 26px;
  }

  /* Front: identity and contacts */
  .card-front { top: 520px; background: var(--card-white); }
  .front-waves { position: absolute; inset: 0; }
  .brand {
    position: absolute; left: 48px; top: 150px;
    display: flex; align-items: center; gap: 14px;
    font-family: "Questrial", sans-serif;
    font-size: 38px; color: var(--navy); letter-spacing: 0.5px;
  }
  .brand-dot { width: 22px; height: 22px; border-radius: 50%; background: var(--navy); }
  .website {
    position: absolute; left: 84px; top: 204px;
    font-family: "Questrial", sans-serif;
    font-size: 17px; color: var(--navy); letter-spacing: 0.3px;
  }
  .holder {
    position: absolute; right: 40px; top: 38px;
    font-family: "Questrial", sans-serif; text-align: left;
  }
  .holder-name { font-size: 26px; color: var(--blue); font-variant: small-caps; letter-spacing: 1px; }
  .holder-role { font-size: 16px; color: var(--navy); letter-spacing: 1.5px; }
  .contacts {
    position: absolute; right: 36px; top: 226px;
    list-style: none; font-family: "Questrial", sans-serif;
    font-size: 18px; color: var(--navy);
  }
  .contact-line {
    display: flex; justify-content: flex-end; align-items: center;
    gap: 14px; height: 34px; text-align: right; white-space: nowrap;
  }
  .contact-line.address-first { height: 30px; }
  .contact-line.address-last { padding-right: 40px; }
  .icon { width: 26px; height: 26px; flex: none; }
</style>
</head>
<body>
<main class="stage">

  <section class="card card-back" aria-label="Card back: product range">
    <ul class="product-list">
      <li>- Stainless Steel Refrigeration Doors</li>
      <li>- Double &amp; Triple Glazed Refrigeration Doors</li>
      <li>- Heated Glass Refrigeration Doors</li>
      <li>- Inserts for both Under-bar and Coolroom</li>
      <li>- Single &amp; Double Glazed Sliding Doors</li>
      <li>- Super View Panels</li>
      <li>- Hood Light Covers</li>
      <li>- LED and Fluro Lights for Cold Food &amp; Cake Display</li>
      <li>- Heat Lamps for Bain-marie and Pies</li>
    </ul>
  </section>

  <section class="card card-front" aria-label="Card front: contact details">
    <svg class="front-waves" viewBox="0 0 810 450" preserveAspectRatio="none" aria-hidden="true">
      <path d="M0 340 C190 370 350 330 480 255 C580 195 700 172 810 168 L810 450 L0 450 Z" fill="var(--sage)"/>
      <path d="M0 315 C180 350 340 315 470 232 C570 172 690 148 810 140" fill="none" stroke="var(--band-grey)" stroke-width="14"/>
      <path d="M0 330 C190 362 350 328 478 246 C578 186 700 162 810 156" fill="none" stroke="var(--sage-soft)" stroke-width="6"/>
      <path d="M0 420 C170 405 300 370 420 310 C520 262 640 220 810 205" fill="none" stroke="#ffffff" stroke-width="10" opacity="0.85"/>
      <path d="M0 440 C160 430 300 400 430 340" fill="none" stroke="var(--band-grey)" stroke-width="8" opacity="0.6"/>
    </svg>

    <div class="brand"><span class="brand-dot"></span>Corvane Doors</div>
    <p class="website">www.corvanedoors-example.com.au</p>

    <div class="holder">
      <p class="holder-name">Brent Oakley</p>
      <p class="holder-role">PROPRIETOR</p>
    </div>

    <ul class="contacts">
      <li class="contact-line address-first">417 Harwick Vale Rd,
        <svg class="icon" viewBox="0 0 26 26" aria-label="Address"><circle cx="13" cy="13" r="13" fill="var(--navy)"/><path d="M13 6a5 5 0 0 0-5 5c0 4 5 9 5 9s5-5 5-9a5 5 0 0 0-5-5z" fill="#fff"/><circle cx="13" cy="11" r="2" fill="var(--navy)"/></svg>
      </li>
      <li class="contact-line address-last">Tamsley, NSW 2874</li>
      <li class="contact-line">(02) 4893 5100
        <svg class="icon" viewBox="0 0 26 26" aria-label="Phone"><circle cx="13" cy="13" r="13" fill="var(--navy)"/><path d="M9 7l3 3-1.5 2a8 8 0 0 0 3.5 3.5l2-1.5 3 3-2 2c-5 0-10-5-10-10z" fill="#fff"/></svg>
      </li>
      <li class="contact-line">(02) 4893 5177
        <svg class="icon" viewBox="0 0 26 26" aria-label="Fax"><circle cx="13" cy="13" r="13" fill="var(--navy)"/><rect x="9" y="6" width="8" height="5" fill="#fff"/><rect x="6" y="11" width="14" height="7" rx="1.5" fill="#fff"/><rect x="9" y="15" width="8" height="5" fill="#fff" stroke="var(--navy)" stroke-width="1"/></svg>
      </li>
      <li class="contact-line">0400 58 3232
        <svg class="icon" viewBox="0 0 26 26" aria-label="Mobile"><circle cx="13" cy="13" r="13" fill="var(--navy)"/><rect x="9" y="5.5" width="8" height="15" rx="1.5" fill="#fff"/><rect x="10.3" y="7.5" width="5.4" height="9" fill="var(--navy)"/><circle cx="13" cy="18.6" r="0.9" fill="var(--navy)"/></svg>
      </li>
      <li class="contact-line">brent@corvanedoors-example.com.au
        <svg class="icon" viewBox="0 0 26 26" aria-label="Email"><circle cx="13" cy="13" r="13" fill="var(--navy)"/><rect x="6" y="8" width="14" height="10" rx="1" fill="#fff"/><path d="M6.5 8.5L13 14l6.5-5.5" fill="none" stroke="var(--navy)" stroke-width="1.3"/></svg>
      </li>
    </ul>
  </section>

</main>
</body>
</html>
```